Flyer Required for Economics Tuition business in Singapore

Require a 4-page, A4 bi-fold full colour flyer. To use attractive & vibrant colours. Can make use of colour schemes and design layouts from upcoming website revamp: http://lessonbrightpath.com/Website/
Target audience for the flyer will be 17 - 18 years old A Level students in Singapore studying in Junior Colleges.
I have attached the detailed design brief with the content required for the flyer as a file titled "Design Brief.docx" & also the logo for our business to be used in the flyer & optional photos that can be used in the flyer
Reason: Require more designs. Current designs provided are too "template" like

```html
<!DOCTYPE html>
<html lang="en">
<head>
<meta charset="utf-8">
<title>Economics Tuition Flyer – Inner Spread</title>
<link rel="stylesheet" href="https://fonts.googleapis.com/css2?family=Open+Sans:ital,wght@0,400;0,700;1,400&family=Roboto+Slab:wght@800&display=swap">
<style>
  :root {
    --canvas: #ecebe8;
    --orange: #f7941d;
    --orange-deep: #e07b12;
    --pink: #e8457c;
    --blue: #1b75bb;
    --green: #8dc63f;
    --navy: #1c2a4a;
    --white: #ffffff;
    --ink: #222222;
    --photo-a: #7d8aa0;
    --photo-b: #c9b7a6;
  }
  html, body { margin: 0; padding: 0; width: 1200px; height: 1000px; overflow: hidden; background: var(--canvas); }
  .spread { position: absolute; left: 50px; top: 110px; width: 1100px; height: 780px; overflow: hidden; box-shadow: 0 8px 24px rgba(0,0,0,.25); font-family: "Open Sans", Arial, sans-serif; }
  .spread-bg { position: absolute; inset: 0; }
  .founder { position: absolute; left: 28px; top: 28px; width: 492px; color: var(--white); }
  .founder-title { font-family: "Roboto Slab", Georgia, serif; font-weight: 800; font-size: 21px; text-align: center; margin: 0 0 18px; }
  .founder h3 { font-size: 12.5px; font-weight: 700; margin: 12px 0 1px; }
  .founder p { font-size: 11.5px; line-height: 1.35; margin: 0; }
  .photo { position: absolute; border-radius: 50%; }
  .photo-founder { left: 130px; top: 520px; width: 440px; height: 235px; border: 4px solid var(--pink); background: linear-gradient(135deg, var(--photo-b), var(--photo-a)); }
  .photo-students { left: 640px; top: 22px; width: 360px; height: 190px; border: 4px solid var(--blue); background: linear-gradient(135deg, var(--photo-a), var(--photo-b)); }
  .testimonials-title { position: absolute; left: 590px; top: 294px; margin: 0; font-family: "Roboto Slab", Georgia, serif; font-weight: 800; font-size: 17px; color: var(--navy); }
  .quote-column { position: absolute; display: flex; flex-direction: column; gap: 8px; }
  .col-left { left: 562px; top: 324px; width: 272px; }
  .col-right { left: 848px; top: 230px; width: 238px; }
  .quote { box-sizing: border-box; margin: 0; background: var(--white); border: 2px solid var(--pink); border-radius: 9px; padding: 6px 10px 5px; color: var(--ink); box-shadow: 0 2px 4px rgba(0,0,0,.2); }
  .quote p { margin: 0; font-size: 9px; line-height: 1.25; }
  .quote.is-small p { font-size: 7.2px; line-height: 1.25; }
  .quote cite { display: block; text-align: right; font-style: normal; font-size: 8.5px; line-height: 1.25; margin-top: 3px; }
</style>
</head>
<body>
<main class="spread">
  <svg class="spread-bg" width="1100" height="780" viewBox="0 0 1100 780" aria-hidden="true">
    <defs>
      <linearGradient id="spine" x1="0" x2="1">
        <stop offset="0" stop-color="#f7941d"/>
        <stop offset="1" stop-color="#d9720f"/>
      </linearGradient>
    </defs>
    <rect x="0" y="0" width="1100" height="780" fill="#ffffff"/>
    <rect x="0" y="0" width="550" height="780" fill="var(--orange)"/>
    <path d="M500,0 L720,0 C660,110 610,230 560,380 L500,420 Z" fill="url(#spine)"/>
    <path d="M700,0 L1100,0 L1100,320 C960,250 800,250 640,320 C670,200 690,90 700,0 Z" fill="var(--pink)"/>
    <path d="M760,0 C900,120 1000,200 1100,230" stroke="#f27aa3" stroke-width="6" fill="none" opacity=".6"/>
    <path d="M400,780 C430,620 480,520 560,470 C700,390 900,420 1100,430 L1100,780 Z" fill="var(--blue)"/>
    <path d="M555,470 C700,395 900,420 1100,430" stroke="#ffffff" stroke-width="6" fill="none"/>
    <path d="M0,560 C30,690 140,760 300,780 L0,780 Z" fill="var(--blue)"/>
    <path d="M0,520 C40,680 170,760 330,780" stroke="var(--green)" stroke-width="16" fill="none"/>
    <path d="M510,470 C530,420 555,380 590,350" stroke="var(--green)" stroke-width="12" fill="none"/>
    <rect x="548" y="0" width="4" height="780" fill="#000" opacity=".08"/>
  </svg>

  <section class="founder">
    <h2 class="founder-title">About our Programme Founder</h2>
    <h3>Background</h3>
    <p>Mr Ethan Low is the Programme Founder &amp; Managing Director for Economics At LessonBrightPath Pte Ltd. He also owns and manages CLEAR Education Centre &amp; IdeaHub Learning Centre.</p>
    <h3>Academic Qualifications</h3>
    <p>Mr Low loves and specialises in Economics and he obtained his Bachelor of Arts in Economics from the Harbourview University (HVU). He is also currently doing his Masters in Applied Economics at the Lakeside Management University (LMU) and he intends to pursue further studies in Economics after his Masters.</p>
    <h3>Teaching Experience</h3>
    <p>Mr Low has established a unique tuition programme under the name of Economics at LessonBrightPath since 2007. Each year he tutors about 150-200 on average and many of his students were top students in their classes and level for Economics. (read the testimonials!) That means more than a thousand students have gone through Mr Low's intensive Economics tuition programme!</p>
    <h3>Style of Teaching</h3>
    <p>Mr Low is different from other tutors because he employs a mixture of strategies to help the student excel. He thinks that for a student to excel in a subject, he must first be interested in the subject, and that's why Mr Low tries to make his lessons interesting and relatable to the student. He also looks at the syllabus holistically and reverse engineers the methods to do well for the examination by ensuring that the appropriate right amount of content is covered without compromising on the quality of the learning. Through weekly discussions and looking at real-world problems, Mr Low also helps his students discover the essential application skills that are required to score that Distinction in the A Levels.</p>
  </section>

  <div class="photo photo-founder" role="img" aria-label="Group photo of students seated and standing with their tutor"></div>
  <div class="photo photo-students" role="img" aria-label="Group photo of cheerful students posing in a classroom"></div>

  <h2 class="testimonials-title">Testimonials From Students</h2>

  <div class="quote-column col-left">
    <blockquote class="quote">
      <p>“Mr Low really has all his students' interests at heart. He buys dinner for us, provide us with mini snacks, incentivise us with great rewards; there was also once when he bought me some flu medicine because I was suffering from a bad cold thank you Mr Low!”</p>
      <cite>Hana Lee Wen<br>Westbrook Junior College</cite>
    </blockquote>
    <blockquote class="quote">
      <p>“Mr Low is a very friendly teacher who ensures that his students receive the best. He spends a lot of effort in preparing for lessons such as finding articles that are relevant to the subject and coming up with different ways to help us learn better.”</p>
      <cite>Ang Rui Jie<br>Meridian Junior College</cite>
    </blockquote>
    <blockquote class="quote is-small">
      <p>“Mr Low's lessons are very engaging and fun. It's a very different and beneficial tuition style that will definitely benefit students. Content was covered very effectively and thoroughly for each lesson and made easy to understand by Mr Low's effective teaching methods and anecdotal examples. There is a very comfortable environment here as everyone is friendly and there are free refreshments. It has been very enjoyable being in this tuition and Mr Low is a wonderful tutor.”</p>
      <cite>Hong Yi Lin<br>Riverside High School</cite>
    </blockquote>
    <blockquote class="quote">
      <p>“Even though I have only been working with Mr Low for a few months, I have learnt many different skills and specific Singaporean examples that are essential for a good economic grade, but not covered in school classes. Mr Low also has amazing stories to tell, and I personally am inspired by his 'pilot' story.”</p>
      <cite>Kevin Tan<br>Summit Hill Institution</cite>
    </blockquote>
  </div>

  <div class="quote-column col-right">
    <blockquote class="quote is-small">
      <p>“Mr Low and the tuition centre has greatly improved my quality of work in economics and his knowledge and insights provided during lessons were very valuable to me. I was able to perform well in almost all my examinations after attending lessons and this gave me confidence going into the A levels. I would recommend this tuition centre to those in need of help in econs. You can acquire relevant skills in essays and CSQs which I believe will help me get into A levels with ease.”</p>
      <cite>Max Lim<br>Eastfield Junior College</cite>
    </blockquote>
    <blockquote class="quote">
      <p>“Mr Low is a very friendly and approachable tutor who makes economic concepts much easier to understand. His lessons are very well paced and effective and it has helped me increased my school test grades by 2 grades. Tuition@LessonBrightPath has been fun and very helpful.”</p>
      <cite>Ng Yi Xuan<br>Summit Hill Institution</cite>
    </blockquote>
    <blockquote class="quote">
      <p>“Mr Low is a very engaging tutor who never fail to pique our interest and curiosity over the economics concepts and current economic situation. He makes an effort to make interesting analogies to ensure that his students understand certain concepts thoroughly. Kudos!”</p>
      <cite>Rachel Teo Zhi Min<br>Summit Hill Institution</cite>
    </blockquote>
    <blockquote class="quote">
      <p>“I find Mr Low a committed tutor who does research to provide us with many economics articles and practices for the class. I get much more fruitful practices on essays and case studies during lessons from the group discussions and timed practices that allow me to gauge my understanding of the topic. Thanks Mr Low for providing such a unique tuition experience!”</p>
      <cite>Emma Ong Jia Hui<br>Northpoint Junior College</cite>
    </blockquote>
  </div>
</main>
</body>
</html>
```